" Atendimento personalizado as necessidades do cliente em todos os ramos de tradução. Assistência 24h com plataforma online. Garantindo a segurança de toda documentação pela QTR, Pex, Velkor. "

```html
<!DOCTYPE html>
<html lang="pt-BR">
<head>
<meta charset="UTF-8">
<title>Arvena Traduções — Papel Timbrado</title>
<link href="https://fonts.googleapis.com/css2?family=Cinzel:wght@500&family=Open+Sans:wght@400;600&display=swap" rel="stylesheet">
<style>
  :root {
    --navy: #1f3557;
    --sky: #6fb3de;
    --paper: #ffffff;
    --backdrop: #e6e7e9;
    --footer-text: #d7e2ef;
  }
  html, body {
    margin: 0;
    padding: 0;
    width: 1200px;
    height: 1200px;
    overflow: hidden;
    background: var(--backdrop);
  }
  .letterhead {
    position: absolute;
    left: 225px;
    top: 68px;
    width: 750px;
    height: 1064px;
    background: var(--paper);
    box-shadow: 0 2px 10px rgba(0,0,0,0.12);
    display: flex;
    flex-direction: column;
    font-family: "Open Sans", sans-serif;
  }
  .letterhead__header {
    height: 186px;
    background: var(--navy);
    display: flex;
    flex-direction: column;
    align-items: center;
    padding-top: 22px;
    box-sizing: border-box;
  }
  .brand__dot {
    width: 40px;
    height: 40px;
    border-radius: 50%;
    background: var(--sky);
  }
  .brand__name {
    margin-top: 16px;
    font-family: "Cinzel", serif;
    font-weight: 500;
    font-size: 34px;
    letter-spacing: 1px;
    color: #ffffff;
    line-height: 1;
  }
  .brand__tagline {
    margin-top: 6px;
    font-family: "Cinzel", serif;
    font-size: 9px;
    letter-spacing: 9px;
    color: var(--sky);
    padding-left: 9px;
  }
  .letterhead__body {
    flex: 1;
  }
  .letterhead__footer {
    height: 70px;
    background: var(--navy);
    color: var(--footer-text);
    font-size: 9.5px;
    position: relative;
  }
  .contact {
    position: absolute;
    top: 12px;
    display: flex;
    align-items: flex-start;
    gap: 6px;
    line-height: 1.3;
  }
  .contact--phone { left: 122px; }
  .contact--mail { left: 302px; }
  .contact--address { left: 470px; }
  .contact__icon {
    width: 12px;
    height: 12px;
    flex: none;
  }
  .website {
    position: absolute;
    left: 0;
    right: 0;
    bottom: 9px;
    text-align: center;
    font-size: 10.5px;
  }
  .letterhead__stripe {
    height: 10px;
    background: var(--sky);
  }
</style>
</head>
<body>
  <main class="letterhead">
    <header class="letterhead__header">
      <span class="brand__dot"></span>
      <div class="brand__name">ARVENA</div>
      <div class="brand__tagline">TRADUÇÕES</div>
    </header>

    <section class="letterhead__body"></section>

    <footer class="letterhead__footer">
      <div class="contact contact--phone">
        <svg class="contact__icon" viewBox="0 0 12 12"><circle cx="6" cy="6" r="6" fill="#6fb3de"/><path d="M4 3.2c.3-.2.6 0 .7.3l.4 1c.1.3 0 .5-.2.7l-.3.2c.3.7.8 1.2 1.5 1.5l.2-.3c.2-.2.4-.3.7-.2l1 .4c.3.1.5.4.3.7-.3.6-.9.9-1.6.7C5 7.8 4.2 7 3.7 5.3c-.2-.8.1-1.6.3-2.1z" fill="#1f3557"/></svg>
        <span>99 9 9999 99 99 | 9999 99 99</span>
      </div>
      <div class="contact contact--mail">
        <svg class="contact__icon" viewBox="0 0 12 12"><circle cx="6" cy="6" r="6" fill="#6fb3de"/><rect x="3" y="4" width="6" height="4.2" fill="none" stroke="#1f3557" stroke-width="0.9"/><path d="M3 4l3 2.3L9 4" fill="none" stroke="#1f3557" stroke-width="0.9"/></svg>
        <span>contato@arvena.com.br</span>
      </div>
      <div class="contact contact--address">
        <svg class="contact__icon" viewBox="0 0 12 12"><circle cx="6" cy="6" r="6" fill="#6fb3de"/><path d="M6 2.6a2 2 0 0 1 2 2c0 1.5-2 4-2 4s-2-2.5-2-4a2 2 0 0 1 2-2z" fill="#1f3557"/><circle cx="6" cy="4.6" r="0.7" fill="#6fb3de"/></svg>
        <span>Rua das Arvenas, 9999 | Centro<br>Sala 1000 - CEP: 55.555-555<br>Cidade - UF</span>
      </div>
      <div class="website">www.arvena.com.br</div>
    </footer>
    <div class="letterhead__stripe"></div>
  </main>
</body>
</html>
```